Banners for a bowtie/tie Fashion shop

I need banners (770x100) for a necktie and bowtie shop (http://www.kelorin.dk)

5 BOWTIE BANNERS:

I need the 3 text versions for eatch bowtie banner:

Danmarks største udvalg af butterfly
Køb butterfly. FRI fragt og FRI retur
Butterfly fra 199,- inkl. FRI fragt

5 NECKTIE BANNERS:

I need the 3 text versions for eatch necktie banner:

Danmarks største udvalg af slips
Køb slips. FRI fragt og FRI retur
Slips fra 199,- inkl. FRI fragt

All banners should contain the logo. All in JPG format and Photoshop/Inddesign/illustrator format

Target Market(s)

Guys and Gays

Industry/Entity Type

Shop

Requirements
Must have
• Logo
Nice to have
• Nice new pictures

```html
<!DOCTYPE html>
<html lang="da">
<head>
<meta charset="utf-8">
<title>Kelorin bannere</title>
<link href="https://fonts.googleapis.com/css2?family=Montserrat:wght@300;400;500;600&display=swap" rel="stylesheet">
<style>
  :root {
    --page-bg: #eceef1;
    --banner-black: #050505;
    --banner-dark-a: #141416;
    --banner-dark-b: #2a2b31;
    --divider: #2c2c2e;
    --text-main: #ffffff;
    --text-muted: #8c8c8c;
    --photo-dark: #1a1a1c;
    --photo-mid: #4a4a4e;
  }
  * { margin: 0; padding: 0; box-sizing: border-box; }
  html, body {
    width: 986px; height: 1200px; overflow: hidden;
    background: var(--page-bg);
    font-family: "Montserrat", Arial, sans-serif;
  }
  .banner {
    position: absolute; left: 71px; width: 844px; height: 110px;
    overflow: hidden; color: var(--text-main);
  }
  .banner--bowtie { background: linear-gradient(90deg, var(--banner-dark-a), var(--banner-dark-b) 70%, var(--banner-dark-a)); }
  .banner--tie { background: var(--banner-black); }
  .brand {
    position: absolute; left: 19px; top: 0; width: 182px; height: 110px;
    display: flex; align-items: center; justify-content: center;
    font-size: 44px; font-weight: 500; letter-spacing: -0.5px; color: var(--text-main);
  }
  .divider {
    position: absolute; left: 219px; top: 12px; width: 1px; height: 86px;
    background: var(--divider);
  }
  .message {
    position: absolute; top: 0; height: 110px;
    display: flex; flex-direction: column; align-items: center; justify-content: center;
    text-align: center; line-height: 1.05;
  }
  .banner--bowtie .message { left: 220px; width: 350px; }
  .banner--tie .message { left: 220px; width: 400px; }
  .headline { font-size: 35px; font-weight: 600; }
  .headline--light { font-size: 26px; font-weight: 400; letter-spacing: 0.3px; line-height: 1.22; }
  .headline--stack { font-size: 31px; font-weight: 600; line-height: 1.05; }
  .headline .light { font-weight: 400; }
  .subline { font-size: 20px; font-weight: 400; color: var(--text-muted); margin-top: 6px; letter-spacing: 0.5px; }
  .subline--ruled { border-top: 1px solid var(--text-muted); border-bottom: 1px solid var(--text-muted); padding: 0 6px; margin-top: 6px; }
  .photo { position: absolute; top: 0; right: 0; height: 110px; }
  .photo--bowtie { width: 274px; background: linear-gradient(90deg, rgba(20,20,22,0), var(--photo-dark) 25%, var(--photo-mid) 50%, var(--photo-dark) 75%); }
  .photo--tie { width: 223px; background: linear-gradient(90deg, var(--photo-dark), var(--photo-mid) 55%, var(--photo-dark)); }
</style>
</head>
<body>

<div class="banner banner--bowtie" style="top:78px">
  <div class="brand">kelorin</div><div class="divider"></div>
  <div class="message">
    <div class="headline">KØB BUTTERFLY</div>
    <div class="subline">FRI fragt og FRI retur</div>
  </div>
  <div class="photo photo--bowtie" role="img" aria-label="Mand i smoking med sort butterfly"></div>
</div>

<div class="banner banner--bowtie" style="top:243px">
  <div class="brand">kelorin</div><div class="divider"></div>
  <div class="message">
    <div class="headline headline--light">DANMARKS STØRSTE<br>UDVALG AF BUTTERFLY</div>
  </div>
  <div class="photo photo--bowtie" role="img" aria-label="Mand i smoking med sort butterfly"></div>
</div>

<div class="banner banner--bowtie" style="top:403px">
  <div class="brand">kelorin</div><div class="divider"></div>
  <div class="message">
    <div class="headline headline--stack">BUTTERFLY<br>FRA 199,- <span class="light">inkl.</span></div>
    <div class="subline" style="margin-top:2px">FRI fragt</div>
  </div>
  <div class="photo photo--bowtie" role="img" aria-label="Mand i smoking med sort butterfly"></div>
</div>

<div class="banner banner--tie" style="top:653px">
  <div class="brand">kelorin</div><div class="divider"></div>
  <div class="message">
    <div class="headline headline--stack">DANMARKS STØRSTE<br>UDVALG AF SLIPS</div>
  </div>
  <div class="photo photo--tie" role="img" aria-label="Mand i mørkt jakkesæt med stribet slips"></div>
</div>

<div class="banner banner--tie" style="top:827px">
  <div class="brand">kelorin</div><div class="divider"></div>
  <div class="message">
    <div class="headline">SLIPS FRA 199,- <span class="light">inkl.</span></div>
    <div class="subline subline--ruled">FRI fragt</div>
  </div>
  <div class="photo photo--tie" role="img" aria-label="Mand i mørkt jakkesæt med stribet slips"></div>
</div>

<div class="banner banner--tie" style="top:993px">
  <div class="brand">kelorin</div><div class="divider"></div>
  <div class="message">
    <div class="headline">KØB SLIPS</div>
    <div class="subline">FRI fragt og FRI retur</div>
  </div>
  <div class="photo photo--tie" role="img" aria-label="Mand i mørkt jakkesæt med stribet slips"></div>
</div>

</body>
</html>
```